Direct Mail Campaign for Safety Supply Company

Design a 6 inch x 11 inch direct mail piece targeting business contacts that purchase PPE (personal protection equipment) such as safety gloves, glasses, hard hats, vests, etc. <br/><br/>Target - Many different contacts in a business might be the buyer such as Safety Manager, Office Manager, Warehouse worker, etc. <br/><br/>Location - Will mail to business in Dallas close to their distribution warehouse at 2318 Marbury Ave Ste 40, Dallas, TX 75219<br/><br/>Competitive Advantages<br/>Speed - can deliver next day and in emergencies, potentially same day.<br/>Service - ability to speak directly to a person instead of being caught online<br/>Convenience - easy to work with<br/>Consultation - assistance with finding the right solutions for prospects company, increasing engagement and usage, employee satisfaction.

Target Market(s)

Contacts within a company that purchase personal protection equipment. It is a wide array of companies and contacts. Direct mail design should be either catchy or clever.

Industry/Entity Type

Safety

Font styles to use
Sans Serif

Colors

Designer to choose colors to be used in the design.

Requirements
Must have
• Front should have a great visual image with company logo and a short statement or tag line.
• Back should speak to reasons why they should try PWT. Leave 4" wide x 2" tall space for inkjetting on lower right.
Nice to have
• Open to ideas.

```html
<!DOCTYPE html>
<html lang="en">
<head>
<meta charset="utf-8">
<title>PWT Safety Supplies – Direct Mail</title>
<link rel="stylesheet" href="https://fonts.googleapis.com/css2?family=Anton&family=League+Gothic&display=swap">
<style>
  :root{
    --red:#ab3640;
    --red-deep:#972b35;
    --red-photo:#b9575f;
    --cream:#f4efe6;
    --white:#ffffff;
    --ink:#1a1a1a;
    --paper:#ffffff;
  }
  *{margin:0;padding:0;box-sizing:border-box}
  html,body{width:1200px;height:1104px;overflow:hidden;background:var(--paper)}
  .mailer{position:relative;width:1200px;height:1104px}
  .backdrop{position:absolute;inset:0}
  .txt{position:absolute;line-height:1;white-space:nowrap;text-align:center}
  .brand{font-family:"Anton",sans-serif;font-weight:400}
  .cond{font-family:"League Gothic","Oswald",sans-serif;font-weight:400;text-transform:uppercase}

  /* back panel */
  .back .brand-name{left:111px;top:82px;width:411px;font-size:155px;color:var(--white);letter-spacing:50px;padding-left:50px}
  .back .brand-sub{left:111px;top:235px;width:411px;font-size:47px;color:var(--white);letter-spacing:5.5px;padding-left:5.5px}
  .benefit-title{color:var(--white)}
  .benefit-note{color:var(--white)}
  .delivery .benefit-title{left:50px;top:342px;width:400px;font-size:56px}
  .delivery .benefit-note{left:50px;top:393px;width:400px;font-size:42px;letter-spacing:-2.3px}
  .consult .benefit-title{left:135px;top:519px;width:440px;font-size:54px;letter-spacing:1.5px}
  .consult .benefit-note{left:137px;top:569px;width:440px;font-size:41px;letter-spacing:-2px}
  .satisfy .benefit-title{left:48px;top:680px;width:440px;font-size:54px;letter-spacing:1px}
  .satisfy .benefit-note{left:46px;top:730px;width:440px;font-size:42px;letter-spacing:-2.6px}
  .slogan{left:25px;top:853px;width:190px;font-size:48px;line-height:43px;color:var(--white);white-space:nowrap}
  .address{left:217px;top:851px;width:383px;font-size:40px;color:var(--white);text-align:right;letter-spacing:-3px}

  /* front panel */
  .front .brand-name{left:772px;top:99px;width:380px;font-size:126px;color:var(--ink);letter-spacing:40px;padding-left:40px}
  .front .brand-sub{left:772px;top:223px;width:380px;font-size:37px;color:var(--ink);letter-spacing:5.7px;padding-left:5.7px}
  .hero-word{left:660px;top:699px;width:470px;font-size:218px;color:var(--cream)}
  .hero-line{left:657px;width:470px;font-size:61px;color:var(--cream)}
  .hero-line.one{top:915px}
  .hero-line.two{top:969px}
</style>
</head>
<body>
<main class="mailer">
  <svg class="backdrop" viewBox="0 0 2000 1840" width="1200" height="1104">
    <!-- back panel -->
    <rect x="42" y="40" width="959" height="1760" fill="var(--red)"/>
    <polygon points="42,470 1001,70 1001,150 42,510" fill="var(--red-deep)"/>
    <g role="img" aria-label="Faded photo of a worker in hard hat, safety glasses and hi-vis vest">
      <polygon points="42,510 1001,150 1001,1000 42,1340" fill="var(--red-photo)" opacity="0.85"/>
    </g>
    <polygon points="42,1340 1001,1000 1001,1030 42,1375" fill="var(--red-deep)"/>
    <g role="img" aria-label="Orange cut-resistant work glove">
      <rect x="745" y="525" width="140" height="235" rx="40" fill="#e07a3a"/>
    </g>
    <g role="img" aria-label="Yellow hard hat">
      <ellipse cx="134" cy="940" rx="86" ry="62" fill="#f2cf1f"/>
    </g>
    <g role="img" aria-label="Grey tinted safety glasses">
      <ellipse cx="855" cy="1250" rx="100" ry="45" fill="#5d5f62"/>
    </g>
    <rect x="356" y="1492" width="645" height="308" fill="var(--paper)"/>

    <!-- front panel -->
    <rect x="1007" y="40" width="959" height="1760" fill="var(--red)"/>
    <defs>
      <linearGradient id="site" x1="0" y1="0" x2="0" y2="1">
        <stop offset="0" stop-color="#e9e9e6"/>
        <stop offset="0.55" stop-color="#c9c2b2"/>
        <stop offset="0.75" stop-color="#7d8a5e"/>
        <stop offset="1" stop-color="#8a7256"/>
      </linearGradient>
    </defs>
    <polygon points="1007,420 1966,60 1966,125 1007,490" fill="var(--red-deep)"/>
    <g role="img" aria-label="Photo of construction workers in hard hats and harnesses on a steel beam, one swinging a sledgehammer">
      <polygon points="1007,490 1966,125 1966,1120 1007,1480" fill="url(#site)"/>
    </g>
    <polygon points="1007,1480 1966,1120 1966,1160 1007,1520" fill="var(--red-deep)"/>
  </svg>

  <section class="back">
    <div class="txt brand brand-name">PWT</div>
    <div class="txt brand brand-sub">SAFETY SUPPLIES</div>

    <div class="benefit delivery">
      <div class="txt cond benefit-title">Next Day Delivery</div>
      <div class="txt cond benefit-note">And Emergency Same Day Delivery</div>
    </div>
    <div class="benefit consult">
      <div class="txt cond benefit-title">Business Consultation</div>
      <div class="txt cond benefit-note">Find the Right Solution for Your Company</div>
    </div>
    <div class="benefit satisfy">
      <div class="txt cond benefit-title">Employee Satisfaction</div>
      <div class="txt cond benefit-note">Increasing Engagement and Usage</div>
    </div>

    <p class="txt cond slogan">Safety<br>isn’t<br>expensive,<br>it’s<br>priceless</p>
    <p class="txt cond address">2318 Marbury Ave Ste 40, Dallas, TX 75219</p>
  </section>

  <section class="front">
    <div class="txt brand brand-name">PWT</div>
    <div class="txt brand brand-sub">SAFETY SUPPLIES</div>
    <h1 class="txt cond hero-word">Safety</h1>
    <p class="txt cond hero-line one">Comes when you use the</p>
    <p class="txt cond hero-line two">right supplies</p>
  </section>
</main>
</body>
</html>
```